Venue Booking Site

I would like a venue directory and booking website designed. The idea is that end users will come to the site to find venues for weddings, parties, events etc. They will be able to find the venue based on many criteria, the most important ones are availability and location - they will be able to see in real time which venues are available for the desired dates and areas.

Venues will be able to use the website as a reservation management tool, receive payments for bookings through the site and be able to manage bookings on the go. This will be made into an app. It needs to be developed in bootstrap. Brand name to be used: Mirqona. Venue, place and space bookings.

Target audience - end users - anyone who is looking for a venue. For Community members it will provide an easy way to find a suitable venue
Outline what dates and times the venue is available
Outline costs involved in booking the venue
Search via many other criteria
It will allow the customer to book and pay for the venue online in one smooth process

Clients: Venue managers - particularly focussing on not for profit businesses eg, GHAs, community hall managers, small business managers. These people typically use paper based systems yet and do not use websites so it needs to be very user friendly. Future growth to restaurants, pubs, event venues who have a stronger familiarity with computers and who might already use their own booking management tool - so this needs to be able to link in with their system.

What need will this meet for venue managers:
This tool provides venues with greater visibility, promotion and advertising of their venue
This allows more customers to find them and book with them
This tool will be offered to not-for-profit venue managers for free to better connect them to the community
This means greater profit for these community venues
This means more revenue and jobs created in these communities

Sample of the layout / contents attached. This is not a complete site map as yet as it is a work in progress for final pages.

Small Business

5+ page

Sans Serif

eb2027

• This is a psd file only - one template for each different section, home page, search page, detailed page view, admin back end
• does not need to be coded.
• Note, the golden lantern logo jpeg files were files we were toying with using for this project- but I am happy to use the main mirqona logo- I will let you decide.

```html
<!DOCTYPE html>
<html lang="en">
<head>
<meta charset="UTF-8">
<title>Mirqona – Venue Booking</title>
<link href="https://fonts.googleapis.com/css2?family=Arimo:wght@400;700&display=swap" rel="stylesheet">
<style>
  :root {
    --maroon: #8a0a22;
    --brand-red: #eb2027;
    --button-red: #9e1230;
    --tab-red: #a52a44;
    --tab-active: #d98f9f;
    --panel-pink: #deb0b9;
    --header-dark: #1c1c1c;
    --header-mid: #3a3a3a;
    --nav-black: #000000;
    --white: #ffffff;
    --ink: #111111;
  }
  * { box-sizing: border-box; margin: 0; padding: 0; }
  html, body { width: 1200px; height: 1000px; overflow: hidden; }
  body {
    position: relative;
    background: var(--maroon);
    font-family: "Arimo", Arial, sans-serif;
    color: var(--ink);
  }
  .site { position: absolute; left: 82px; top: 30px; width: 1033px; height: 970px; background: var(--white); overflow: hidden; }

  /* Header */
  .site-header {
    position: absolute; left: 0; top: 0; width: 1033px; height: 218px;
    background: linear-gradient(180deg, var(--header-mid) 0%, var(--header-dark) 60%, #111 100%);
    color: var(--white);
  }
  .brand {
    position: absolute; left: 66px; top: 38px; width: 328px; height: 122px;
    background: var(--brand-red); border-radius: 20px;
    display: flex; align-items: center; justify-content: center; gap: 16px;
  }
  .brand-mark { width: 40px; height: 40px; background: var(--white); }
  .brand-name { font-size: 52px; font-weight: 400; color: var(--white); }
  .login-title { position: absolute; left: 404px; top: 5px; font-size: 23px; }
  .field-label { position: absolute; font-size: 24px; }
  .field-input { position: absolute; background: var(--white); height: 21px; }
  .keep-box { position: absolute; left: 474px; top: 79px; width: 17px; height: 16px; background: var(--white); }
  .keep-label { position: absolute; left: 506px; top: 77px; font-size: 17px; }
  .forgot { position: absolute; left: 820px; top: 84px; font-size: 17px; text-decoration: underline; }
  .btn {
    position: absolute; height: 38px; background: var(--button-red); color: var(--white);
    border: 3px solid #c9b99a; font-size: 23px; display: flex; align-items: center; justify-content: center;
    box-shadow: 0 2px 4px rgba(0,0,0,.6);
  }
  .charity { position: absolute; left: 384px; top: 179px; font-size: 24px; }

  /* Hero */
  .hero {
    position: absolute; left: 0; top: 218px; width: 1033px; height: 255px;
    background: linear-gradient(90deg, #8a5a2e 0%, #c98a45 30%, #e6c39a 55%, #d9b48a 75%, #b5683a 100%);
  }

  /* Navigation */
  .main-nav { position: absolute; left: 0; top: 473px; width: 1033px; height: 71px; background: var(--nav-black); }
  .nav-item { position: absolute; top: 18px; color: var(--white); font-size: 30px; }
  .nav-sep { position: absolute; top: 0; width: 1px; height: 71px; background: #5a0c1c; }

  /* Venue detail */
  .venue-thumb {
    position: absolute; left: 35px; top: 634px; width: 217px; height: 189px;
    background: linear-gradient(135deg, #5a2a14 0%, #a0693a 45%, #d9c6a8 70%, #3c5a3a 100%);
  }
  .detail-panel { position: absolute; left: 274px; top: 558px; width: 676px; height: 320px; background: var(--panel-pink); }
  .tab {
    position: absolute; top: 0; height: 34px; background: var(--tab-red); color: var(--ink);
    font-size: 17px; display: flex; align-items: center; justify-content: center;
    border: 2px solid #c77a8a; border-bottom: 3px solid #6a1225;
  }
  .tab.is-active { background: var(--tab-active); border-bottom-color: var(--tab-active); }
  .resources-title { position: absolute; left: 9px; top: 45px; font-size: 17px; }
  .resource-list { position: absolute; left: 114px; top: 71px; list-style: none; font-size: 12px; line-height: 23.2px; }
  .resource-list.secondary { left: 342px; top: 75px; font-size: 14px; line-height: 27px; }
  .btn-request {
    position: absolute; left: 448px; top: 265px; width: 190px; height: 36px;
    background: var(--button-red); color: var(--ink); font-size: 17px;
    border: 3px solid #f3d6dc; box-shadow: 0 2px 4px rgba(0,0,0,.5);
    display: flex; align-items: center; justify-content: center;
  }

  /* Footer */
  .site-footer { position: absolute; left: 0; top: 890px; width: 1033px; height: 80px; }
  .copyright { position: absolute; left: 0; width: 1046px; top: 928px; text-align: center; font-size: 17px; color: var(--ink); }
</style>
</head>
<body>
<div class="site">
  <header class="site-header">
    <div class="brand"><span class="brand-mark"></span><span class="brand-name">mirqona</span></div>
    <div class="login-title">Venue Login :</div>
    <div class="field-label" style="left:455px;top:40px;">User Name</div>
    <div class="field-input" style="left:587px;top:43px;width:162px;"></div>
    <div class="field-label" style="left:767px;top:43px;">Password</div>
    <div class="field-input" style="left:884px;top:45px;width:131px;"></div>
    <div class="keep-box"></div>
    <div class="keep-label">Keep me logged in</div>
    <div class="forgot">Forgot your password?</div>
    <div class="btn" style="left:645px;top:122px;width:124px;">Login</div>
    <div class="btn" style="left:814px;top:122px;width:193px;">List My Venue</div>
    <div class="charity">Total raised for charity :</div>
  </header>

  <div class="hero" role="img" aria-label="Hotel restaurant buffet with fruit bowls, flowers and rows of white-clothed dining tables"></div>

  <nav class="main-nav">
    <span class="nav-item" style="left:26px;">Home</span>
    <span class="nav-sep" style="left:125px;"></span>
    <span class="nav-item" style="left:153px;top:20px;">Venues</span>
    <span class="nav-sep" style="left:287px;"></span>
    <span class="nav-item" style="left:319px;top:20px;">News &amp; Offers</span>
    <span class="nav-sep" style="left:540px;"></span>
    <span class="nav-item" style="left:581px;top:16px;">Inspirations</span>
    <span class="nav-sep" style="left:758px;"></span>
    <span class="nav-item" style="left:790px;">Contact</span>
    <span class="nav-sep" style="left:923px;"></span>
    <span class="nav-item" style="left:949px;top:16px;">FAQ</span>
  </nav>

  <div class="venue-thumb" role="img" aria-label="Breakfast buffet counter with bread baskets and cereal dispensers"></div>

  <section class="detail-panel">
    <div class="tab" style="left:2px;width:236px;">General</div>
    <div class="tab is-active" style="left:240px;width:195px;">Facilities &amp; Resources</div>
    <div class="tab" style="left:438px;width:236px;">Photos</div>
    <div class="resources-title">Resources Available :</div>
    <ul class="resource-list">
      <li>+ Venue Type</li>
      <li>+ Venue Size</li>
      <li>+ Ceiling Height</li>
      <li>+ Venue entry door width</li>
      <li>+ Resources Type</li>
      <li>+ Audio Visual Requirements</li>
      <li>+ Entertainment</li>
      <li>+ Facilities</li>
      <li>+ Decorations</li>
      <li>+ Transportation Options</li>
      <li>+ Staff</li>
    </ul>
    <ul class="resource-list secondary">
      <li>+ Parking Spaces</li>
      <li>+ Packages Available</li>
      <li>+ Customer Rating</li>
    </ul>
    <div class="btn-request">Request Booking</div>
  </section>

  <svg class="site-footer" width="1033" height="80" viewBox="0 0 1033 80">
    <path d="M0 80 Q516 -70 1033 80 Z" fill="var(--maroon)"/>
  </svg>
  <div class="copyright">Copyright &copy; 2014 mirqona</div>
</div>
</body>
</html>
```